Larkmoor Capital Partners need a desert themed website!

We need a web design and development for our informational website for our new company named Larkmoor Capital Partners. We would like it to be desert themed and it can be color or black and white. We would like it to be classy and clean, while also talking to the benefits of investment partner with us.

We're thinking probably a home page with a nice image of a LARKMOOR landscape, then other pages would What we offer our partners page (or other wording if you find something better), a meet the founder page, and a contact us page.

What we offer our partners (or other wording if you think of something better):
Our investors offer an opportunity to families that cannot usually get approved for a mortgage, to be able to become future homeowners. Thus, Benefiting both the investors and local surrounding community members. Our investors get to both have all the benefits of an investment with receiving above market rates of return to themselves and helping families find homes at the same time.

Maybe also build an infographic with these benefits: Safety, Security, Long-term investment horizon, cashflow, tax benefits, above market rate of return, and capital growth.

And a meet the founder page. With my headshot.

Dale Corwith is a private equity investor providing significantly above market returns to his investment partners while taking the time to be involved with his community and family. Dale first honed his skills in taking calculated risk decisions while very young where he took on playing poker professionally. He succeeded at the highest levels for over a decade competing in high stakes professional cash games around the world.

From the poker world he transitioned to investing in public and private markets. He took an approach of knowing the companies he invests in intimately and after over 10,000 hours of research became known in his community as the person to get investment advice on the electric vehicle industry for his voracious research and expert insight.

He now invests in single family homes in the Phoenix market using his past experience analyzing probabilistic outcomes and comparing the ROIs of different potential strategies. These skills have contributed to his success in investing in companies where he used his ability to assess risk to reward ratios to significantly outperform the market over an extended period.

Contact page we want my email Dale@LarkmoorFunds.example, my instagram: @DaleCorwith, and my linkedin https://www.profilehub.example/in/dale-corwith-58172036/

I have included my headshot for the about me page. I've included some saguaro generated images feel free to incorporate into the website (or make them the company logo), or not, whatever you feel gives the best look for the website.

```html
<!DOCTYPE html>
<html lang="en">
<head>
<meta charset="utf-8">
<title>Larkmoor Capital Partners</title>
<link href="https://fonts.googleapis.com/css2?family=Raleway:wght@700;800&family=Inter:wght@400;500;600&display=swap" rel="stylesheet">
<style>
  :root {
    --brown: #9a6232;
    --dark: #222222;
    --ink: #3a3a3a;
    --text: #1f1f1f;
    --white: #ffffff;
    --field: #ececec;
    --field-line: #8d8d8d;
  }
  * { margin: 0; padding: 0; box-sizing: border-box; }
  html, body { width: 1200px; height: 3803px; overflow: hidden; background: var(--white); }
  body { position: relative; font-family: "Inter", sans-serif; color: var(--text); }
  .abs { position: absolute; }
  .nav-link { position: absolute; top: 52px; font-size: 13px; font-weight: 500; letter-spacing: .3px; color: var(--text); text-decoration: none; }
  .brand { position: absolute; left: 0; width: 1200px; text-align: center; }
  .brand-dot { display: block; margin: 0 auto; border-radius: 50%; background: linear-gradient(#d7a070, #8a5a3a); }
  .brand-name { font-family: "Raleway", sans-serif; font-weight: 800; color: var(--text); line-height: 1.1; }
  .brand-sub { font-family: "Raleway", sans-serif; font-weight: 800; color: var(--text); }
  .photo { position: absolute; }
  .hero-photo { left: 17px; top: 123px; width: 1166px; height: 387px; background: linear-gradient(#dfe3e6 0%, #cfd3d5 22%, #b98a4f 38%, #a77637 70%, #c9a471 100%); }
  .title { position: absolute; left: 125px; top: 578px; font-family: "Raleway", sans-serif; font-weight: 800; font-size: 68px; line-height: 66px; color: var(--ink); letter-spacing: -.5px; }
  .btn { position: absolute; display: flex; align-items: center; justify-content: center; background: var(--brown); color: var(--white); font-size: 11px; font-weight: 600; letter-spacing: .3px; text-decoration: none; }
  .lead { position: absolute; left: 125px; top: 738px; width: 720px; font-size: 13.5px; line-height: 22px; color: var(--text); }
  .portrait { left: 125px; top: 882px; width: 383px; height: 510px; background: linear-gradient(160deg, #cbb7a0, #9c8572 60%, #7d7570); border: 1px solid #555; }
  .founder-name { position: absolute; left: 555px; top: 912px; font-family: "Raleway", sans-serif; font-weight: 800; font-size: 49px; color: var(--ink); }
  .bio { position: absolute; left: 555px; width: 520px; font-size: 13.2px; line-height: 21.7px; color: var(--text); }
  .offer-panel { position: absolute; left: 17px; top: 1493px; width: 593px; height: 717px; background: var(--dark); }
  .offer-desert { left: 17px; top: 1910px; width: 593px; height: 300px; background: linear-gradient(#2a2626 0%, #5e3f3a 40%, #8a5b4c 65%, #6d5a3c 100%); }
  .offer-meeting { left: 612px; top: 1493px; width: 571px; height: 717px; background: linear-gradient(135deg, #eef0f2 0%, #d8dadd 45%, #7a5a42 75%, #4a3526 100%); }
  .offer-title { position: absolute; left: 125px; top: 1570px; font-family: "Raleway", sans-serif; font-weight: 800; font-size: 48px; line-height: 50px; color: var(--white); }
  .offer-text { position: absolute; left: 125px; top: 1693px; width: 410px; font-size: 13.2px; line-height: 21.7px; color: var(--white); }
  .section-title { position: absolute; font-family: "Raleway", sans-serif; font-weight: 800; font-size: 48px; color: var(--ink); }
  .benefits-text { position: absolute; left: 125px; top: 2369px; width: 520px; font-size: 13.2px; line-height: 21.7px; }
  .tile { position: absolute; width: 147px; height: 147px; background: var(--dark); display: flex; flex-direction: column; align-items: center; justify-content: center; gap: 12px; color: var(--white); font-family: "Raleway", sans-serif; font-weight: 800; font-size: 13px; line-height: 16px; text-align: center; text-transform: uppercase; }
  .tile svg { width: 42px; height: 42px; stroke: var(--brown); fill: none; stroke-width: 1.6; stroke-linecap: round; stroke-linejoin: round; }
  .field { position: absolute; left: 233px; width: 734px; height: 45px; background: var(--field); border: 1px solid var(--field-line); font-size: 12px; color: #555; text-align: center; padding-top: 14px; }
  .field-message { height: 170px; }
  .footer { position: absolute; left: 0; top: 3350px; width: 1200px; height: 372px; background: #161616; }
  .social { position: absolute; top: 3570px; width: 36px; height: 36px; border: 2px solid var(--brown); border-radius: 50%; }
  .foot-link { position: absolute; top: 3641px; font-size: 11.5px; color: var(--white); font-weight: 500; text-decoration: none; }
  .copyright { position: absolute; top: 3755px; left: 0; width: 1200px; text-align: center; font-size: 11.5px; font-weight: 500; }
</style>
</head>
<body>

<header class="site-header">
  <a class="nav-link" style="left:125px" href="#">HOME</a>
  <a class="nav-link" style="left:207px" href="#">FOUNDERS BIO</a>
  <a class="nav-link" style="left:835px" href="#">WHAT WE OFFER</a>
  <a class="nav-link" style="left:988px" href="#">CONTACT US</a>
  <div class="brand" style="top:17px">
    <span class="brand-dot" style="width:62px;height:62px"></span>
    <div class="brand-name" style="font-size:15px;margin-top:8px">LARKMOOR</div>
    <div class="brand-sub" style="font-size:6px">CAPITAL PARTNERS</div>
  </div>
</header>

<div class="photo hero-photo" role="img" aria-label="Desert badlands landscape under a cloudy sky"></div>

<h1 class="title">Larkmoor<br>Capital Partners</h1>
<a class="btn" style="left:905px;top:662px;width:170px;height:40px" href="#">CONTACT US</a>
<p class="lead">We believe in empowering you to achieve your financial goals. Our team of experienced advisors provides tailored investment solutions to help you build and secure your wealth for the future.</p>

<div class="photo portrait" role="img" aria-label="Headshot of founder Dale Corwith"></div>
<h2 class="founder-name">Dale Corwith</h2>
<p class="bio" style="top:997px">He is a private equity investor providing significantly above market returns to his investment partners while taking the time to be involved with his community and family. Dale first honed his skills in taking calculated risk decisions while very young where he took on playing poker professionally. He succeeded at the highest levels for over a decade competing in high stakes professional cash games around the world.</p>
<p class="bio" style="top:1147px">From the poker world he transitioned to investing in public and private markets. He took an approach of knowing the companies he invests in intimately and after over 10,000 hours of research became known in his community as the person to get investment advice on the electric vehicle industry for his voracious research and expert insight.</p>
<a class="btn" style="left:555px;top:1292px;width:170px;height:40px" href="#">READ MORE</a>

<section class="offer">
  <div class="offer-panel"></div>
  <div class="photo offer-desert" role="img" aria-label="Red desert rocks with Joshua trees"></div>
  <div class="photo offer-meeting" role="img" aria-label="Advisor presenting market charts in a meeting room"></div>
  <h2 class="offer-title">What We Offer<br>Our Partners</h2>
  <p class="offer-text">Our investors offer an opportunity to families that cannot usually get approved for a mortgage, to be able to become future homeowners. Thus, Benefiting both the investors and local surrounding community members. Our investors get to both have all the benefits of an investment with receiving above market rates of return to themselves and helping families find homes at the same time.</p>
  <a class="btn" style="left:125px;top:1880px;width:170px;height:40px" href="#">SEE OFFERS</a>
</section>

<section class="benefits">
  <h2 class="section-title" style="left:125px;top:2285px">Benefits</h2>
  <p class="benefits-text">Lorem Ipsum is simply dummy text of the printing and typesetting industry. Lorem Ipsum has been the industry's standard dummy text ever since the 1500s,</p>

  <div class="tile" style="left:927px;top:2150px">
    <svg viewBox="0 0 42 42"><path d="M6 36h30M10 36V26h5v10M18 36V20h5v16M26 36V12h5v24M8 22l22-14M25 8h5v5"/></svg>
    <span>Long-term<br>investment<br>horizon</span>
  </div>
  <div class="tile" style="left:758px;top:2317px">
    <svg viewBox="0 0 42 42"><circle cx="21" cy="21" r="9"/><path d="M21 16v10M18 18h5M18 24h5M21 4v5M21 33v5M4 21h5M33 21h5"/></svg>
    <span>Security</span>
  </div>
  <div class="tile" style="left:927px;top:2317px">
    <svg viewBox="0 0 42 42"><path d="M6 36h30M10 36V28h5v8M18 36V22h5v14M26 36V16h5v20"/><circle cx="14" cy="9" r="3"/><circle cx="22" cy="9" r="3"/><circle cx="30" cy="9" r="3"/></svg>
    <span>Capital<br>growth</span>
  </div>
  <div class="tile" style="left:422px;top:2485px">
    <svg viewBox="0 0 42 42"><path d="M21 5l13 5v10c0 9-6 14-13 17-7-3-13-8-13-17V10z"/><path d="M15 21l4 4 8-8"/></svg>
    <span>Safety</span>
  </div>
  <div class="tile" style="left:590px;top:2485px">
    <svg viewBox="0 0 42 42"><circle cx="21" cy="21" r="11"/><path d="M24 16h-5a2.5 2.5 0 000 5h4a2.5 2.5 0 010 5h-6M21 13v3M21 26v3M6 17a16 16 0 0126-8M36 25a16 16 0 01-26 8"/></svg>
    <span>Cashflow</span>
  </div>
  <div class="tile" style="left:758px;top:2485px">
    <svg viewBox="0 0 42 42"><path d="M10 5h18v32H10zM14 12h10M14 18h10M14 24h6"/><circle cx="30" cy="28" r="6"/><path d="M30 25v6"/></svg>
    <span>Tax benefits</span>
  </div>
  <div class="tile" style="left:927px;top:2485px">
    <svg viewBox="0 0 42 42"><circle cx="21" cy="15" r="9"/><path d="M21 10v10M18 13h5M18 17h5M6 36l8-6h10l5 3M14 30l-3-3"/></svg>
    <span>Above<br>market rate<br>of return</span>
  </div>
</section>

<section class="contact">
  <h2 class="section-title" style="left:0;width:1200px;text-align:center;top:2722px">Get In Touch With Us</h2>
  <div class="field" style="top:2838px">Name</div>
  <div class="field" style="top:2897px">Email</div>
  <div class="field" style="top:2955px">Subject</div>
  <div class="field field-message" style="top:3013px">Message</div>
  <a class="btn" style="left:515px;top:3208px;width:170px;height:42px" href="#">SEND</a>
</section>

<footer>
  <div class="footer"></div>
  <div class="brand" style="top:3417px">
    <span class="brand-dot" style="width:120px;height:120px"></span>
    <div class="brand-name" style="font-size:22px;margin-top:-8px;color:var(--white)">LARKMOOR</div>
    <div class="brand-sub" style="font-size:10px;color:var(--white)">CAPITAL PARTNERS</div>
  </div>
  <a class="social" style="left:556px" href="#" aria-label="Instagram @DaleCorwith"></a>
  <a class="social" style="left:606px" href="#" aria-label="Profile of Dale Corwith"></a>
  <a class="foot-link" style="left:398px" href="#">HOME</a>
  <a class="foot-link" style="left:478px" href="#">ABOUT US</a>
  <a class="foot-link" style="left:583px" href="#">WHAT WE OFFER</a>
  <a class="foot-link" style="left:724px" href="#">CONTACT US</a>
  <p class="copyright">COPYRIGHT@2024-LARKMOOR-ALL RIGHTS RESERVED</p>
</footer>

</body>
</html>
```